Pop-up Banner

Would like a design for a pop-up 85 x 206cm banner for a trade show. (from norla press)
We would like "our logo" (brightwave holdings) - then the tagline - "Your Trusted Partner in Data-Driven Decisions"
*Supporting Bullets*
Unified data, analytics & AI
Trusted insights, faster outcomes
Real-time intelligence at scale
Enterprise-ready, secure solutions
Clarity from data complexity
trusted by...some company logos
Partners with : partner logo
Our Colours: #FFA300, #3D4176, #FDD16E, #F87C57, #A68118, #1C2F36

```html
<!DOCTYPE html>
<html lang="en">
<head>
<meta charset="utf-8">
<title>Brightwave Holdings – Pop-up Banner</title>
<link rel="stylesheet" href="https://fonts.googleapis.com/css2?family=Lexend:wght@400;500;700&family=Arvo:wght@400;700&family=Source+Serif+4:wght@500&display=swap">
<style>
  :root {
    --orange: #FFA300;
    --navy: #3D4176;
    --sand: #FDD16E;
    --coral: #F87C57;
    --ochre: #A68118;
    --ink: #1C2F36;
    --cream: #FDF7EE;
    --page: #E9EDF2;
    --teal: #2E9C8F;
    --sky: #2C8FCB;
  }
  * { box-sizing: border-box; margin: 0; padding: 0; }
  html, body { width: 1200px; height: 1200px; overflow: hidden; background: var(--page); }
  .banner {
    position: absolute; left: 360px; top: 18px; width: 480px; height: 1165px;
    overflow: hidden;
    background: linear-gradient(180deg, #F79A1E 0%, #F8A634 40%, #F9C27A 62%, #FBE3C4 78%, var(--cream) 92%);
    box-shadow: 0 10px 30px rgba(28,47,54,.18);
    font-family: "Lexend", sans-serif; color: var(--navy);
  }
  .decor { position: absolute; inset: 0; pointer-events: none; }
  .brand {
    position: absolute; top: 88px; left: 0; right: 0;
    display: flex; align-items: center; justify-content: center; gap: 18px;
  }
  .brand-dot { width: 84px; height: 84px; border-radius: 50%; background: var(--navy); flex: none; }
  .brand-name { font-weight: 700; font-size: 40px; line-height: 1.02; letter-spacing: .5px; text-transform: uppercase; color: var(--navy); }
  .tagline { position: absolute; top: 262px; left: 0; right: 0; text-align: center; font-family: "Arvo", serif; color: var(--navy); }
  .tagline-lead { font-size: 29px; font-weight: 700; }
  .tagline-key { font-size: 38px; font-weight: 700; line-height: 1.3; margin-top: 6px; }
  .bullets { position: absolute; top: 495px; left: 0; right: 0; list-style: none; text-align: center; }
  .bullets li { font-size: 23px; font-weight: 500; line-height: 47px; color: var(--navy); }
  .bullets li::before { content: "•"; font-size: 16px; margin-right: 10px; vertical-align: 3px; }
  .label {
    position: absolute; left: 50%; transform: translateX(-50%);
    background: var(--navy); color: #fff; border-radius: 14px;
    font-family: "Source Serif 4", serif; font-weight: 500; font-size: 15px; letter-spacing: 1px;
    padding: 4px 14px; text-transform: uppercase; white-space: nowrap;
  }
  .label-trusted { top: 790px; }
  .label-partners { top: 1065px; }
  .logo-row { position: absolute; left: 0; right: 0; display: flex; justify-content: center; align-items: center; gap: 28px; }
  .logo { display: flex; align-items: center; gap: 8px; font-family: "Lexend", sans-serif; font-weight: 500; white-space: nowrap; }
  .logo-mark { width: 26px; height: 26px; border-radius: 50%; flex: none; }
  .logo-mark.square { border-radius: 3px; }
  .row-1 { top: 848px; } .row-2 { top: 905px; } .row-3 { top: 958px; }
  .row-partners { top: 1122px; gap: 20px; }
  .client-ardmoor { color: var(--sky); font-size: 26px; }
  .client-ardmoor .logo-mark { background: var(--sky); }
  .client-kestrel { color: #6B6F78; font-size: 27px; font-weight: 400; }
  .client-kestrel .logo-mark { background: var(--sky); }
  .client-novian { color: var(--navy); font-size: 27px; letter-spacing: 2px; }
  .client-harbour { color: var(--ink); font-size: 16px; font-weight: 700; }
  .client-harbour .logo-mark { background: var(--coral); }
  .client-corvex { color: var(--teal); font-size: 26px; font-weight: 700; }
  .partner { font-size: 20px; }
  .partner .logo-mark { width: 18px; height: 18px; }
  .partner-tallis { color: #5E6268; font-size: 17px; }
  .partner-tallis .logo-mark { background: var(--sky); }
  .partner-quorra { color: #D9312B; font-weight: 700; font-size: 24px; letter-spacing: 1px; }
  .partner-veldt { color: var(--ink); font-weight: 400; font-size: 21px; }
  .partner-northlight { color: #3BA55C; font-size: 15px; }
  .partner-northlight .logo-mark { background: #3BA55C; }
</style>
</head>
<body>
<main class="banner">
  <svg class="decor" viewBox="0 0 480 1165" aria-hidden="true">
    <polygon points="0,690 80,790 0,890" fill="var(--sand)" opacity=".25"/>
    <polygon points="0,780 45,835 0,900" fill="var(--ochre)" opacity=".12"/>
    <polygon points="480,1030 440,1085 480,1130" fill="var(--coral)" opacity=".35"/>
  </svg>

  <header class="brand">
    <span class="brand-dot"></span>
    <span class="brand-name">Brightwave<br>Holdings</span>
  </header>

  <section class="tagline">
    <p class="tagline-lead">"Your Trusted Partner in</p>
    <p class="tagline-key">Data-Driven<br>Decisions"</p>
  </section>

  <ul class="bullets">
    <li>Unified data, analytics &amp; AI</li>
    <li>Trusted insights, faster outcomes</li>
    <li>Real-time intelligence at scale</li>
    <li>Enterprise-ready, secure solutions</li>
    <li>Clarity from data complexity</li>
  </ul>

  <span class="label label-trusted">Trusted by</span>
  <div class="logo-row row-1">
    <span class="logo client-ardmoor"><span class="logo-mark"></span>Ardmoor</span>
  </div>
  <div class="logo-row row-2">
    <span class="logo client-kestrel"><span class="logo-mark square"></span>Kestrel</span>
    <span class="logo client-novian">Novian</span>
  </div>
  <div class="logo-row row-3">
    <span class="logo client-harbour"><span class="logo-mark square"></span>Harbour Quay</span>
    <span class="logo client-corvex">Corvex</span>
  </div>

  <span class="label label-partners">Partners with</span>
  <div class="logo-row row-partners">
    <span class="logo partner partner-tallis"><span class="logo-mark square"></span>Tallis</span>
    <span class="logo partner partner-quorra">QUORRA</span>
    <span class="logo partner partner-veldt">veldt</span>
    <span class="logo partner partner-northlight"><span class="logo-mark"></span>northlight apps</span>
  </div>
</main>
</body>
</html>
```